Büro Vermietung
Aufgabenstellung
Interessenten, welche sich für die Büros oder Gewerbefläche interessieren, sollten auf der Webpage folgende Informationen vorfinden:
Menü-Leiste:
HOME / FLÄCHEN / BILDER / LAGE / KONTAKT
HOME:
Titelbild mit dem Hund & kestral-raeume.ch + Frontbild Liegenschaft
(Zusatztext folgt noch)
FLAECHEN:
Grundriss & Preise
BILDER:
diverse Bilder (folgen noch)
LAGE:
KONTAKT:
(Unsere Adresse) Vermieter /Kontakt
VELNOR IMMOBILEN AG

```html
<!DOCTYPE html>
<html lang="de">
<head>
<meta charset="utf-8">
<title>kestral-raeume.ch – Flächen</title>
<link href="https://fonts.googleapis.com/css2?family=Architects+Daughter&family=Open+Sans:wght@400;600;700&display=swap" rel="stylesheet">
<style>
  :root {
    --brand-red: #cc0a2a;
    --brand-red-dark: #a8001c;
    --brand-purple: #4a4885;
    --purple-light: #a3a2c6;
    --divider: #6e6b9b;
    --text: #4a4a4a;
    --label: #333333;
    --white: #ffffff;
  }
  * { margin: 0; padding: 0; box-sizing: border-box; }
  html, body { width: 1200px; height: 1120px; overflow: hidden; }
  body {
    position: relative;
    font-family: "Open Sans", Verdana, sans-serif;
    color: var(--text);
    background: linear-gradient(to bottom, var(--white) 0, var(--white) 152px, var(--brand-purple) 152px, var(--purple-light) 1120px);
  }
  .topbar { position: absolute; left: 0; top: 114px; width: 1200px; height: 38px; background: var(--brand-red); border-bottom: 2px solid var(--white); }
  .mascot {
    position: absolute; left: 122px; top: 5px; width: 200px; height: 164px;
    background: linear-gradient(to bottom, #c98a4e 0%, #f1ece4 45%, #e8e3d8 80%, #f3e27a 100%);
    border-radius: 90px 90px 6px 6px; z-index: 3;
  }
  .site-name {
    position: absolute; left: 291px; top: 70px; z-index: 3;
    font-family: "Open Sans", Verdana, sans-serif; font-weight: 400; font-size: 26px; line-height: 32px;
    color: var(--text);
  }
  .main-nav { position: absolute; top: 114px; left: 0; width: 1200px; height: 38px; z-index: 2; }
  .main-nav a {
    position: absolute; top: 0; height: 38px; line-height: 38px;
    color: var(--white); text-decoration: none; font-size: 15px; font-weight: 600; text-align: center;
  }
  .main-nav a.active { background: var(--brand-red-dark); }
  .page { position: absolute; left: 120px; top: 152px; width: 961px; height: 968px; background: var(--white); }
  .hero {
    position: absolute; left: 2px; top: 2px; width: 956px; height: 198px;
    background: linear-gradient(100deg, #e4e7ea 0%, #d7dde0 30%, #c8d98a 50%, #e1e4e6 70%, #edeff0 100%);
  }
  .hero-fade { position: absolute; left: 2px; top: 200px; width: 956px; height: 26px; background: linear-gradient(to bottom, #e9eee0, var(--white)); }
  h1, h2 { font-family: "Architects Daughter", cursive; font-weight: 400; color: var(--brand-purple); font-size: 38px; line-height: 1; position: absolute; }
  .copy { position: absolute; font-size: 12px; line-height: 17px; letter-spacing: 0.6px; }
  .building-photo {
    position: absolute; left: 620px; top: 238px; width: 295px; height: 213px;
    background: linear-gradient(to bottom, #3c5ea8 0%, #7f98c6 35%, #d9dde2 55%, #8f9480 80%, #6e6e6e 100%);
  }
  .divider { position: absolute; left: 0; top: 484px; width: 961px; height: 4px; background: var(--divider); }
  .floor-plan {
    position: absolute; left: 37px; top: 527px; width: 223px; height: 201px;
    background: linear-gradient(135deg, #cfe3a3 0%, #f2d9a6 55%, #d7c2a4 100%);
    border: 4px solid #7a7a7a;
  }
  .pdf-button {
    position: absolute; left: 29px; top: 754px; width: 263px; height: 34px;
    background: linear-gradient(to bottom, #e0223f, var(--brand-red-dark));
    color: var(--white); font-size: 11.5px; line-height: 34px; padding-left: 15px; text-decoration: none;
  }
  .pdf-button svg { position: absolute; right: 0; top: 0; }
  .price-group { position: absolute; left: 326px; width: 301px; font-size: 11px; }
  .price-row { height: 17px; line-height: 17px; position: relative; }
  .price-row .label { font-weight: 700; color: var(--label); letter-spacing: 0.4px; }
  .price-row .value { position: absolute; left: 109px; }
  .price-total { position: absolute; right: 0; top: 31px; font-size: 17px; color: var(--brand-purple); }
  .footer {
    position: absolute; left: 2px; top: 927px; width: 956px; height: 37px;
    background: var(--brand-red); color: var(--white); font-size: 11px; line-height: 37px;
  }
  .footer-links { position: absolute; left: 27px; }
  .footer-links span { margin: 0 10px; }
  .copyright { position: absolute; right: 25px; }
</style>
</head>
<body>
  <div class="topbar"></div>
  <div class="mascot" role="img" aria-label="Illustration des Büro-Maskottchens mit Buch und Notizblock"></div>
  <div class="site-name">kestral-raeume.ch</div>

  <nav class="main-nav">
    <a href="#" style="left:571px;width:60px;">HOME</a>
    <a href="#" class="active" style="left:667px;width:92px;">FLÄCHEN</a>
    <a href="#" style="left:791px;width:72px;">BILDER</a>
    <a href="#" style="left:890px;width:60px;">LAGE</a>
    <a href="#" style="left:974px;width:80px;">KONTAKT</a>
  </nav>

  <main class="page">
    <div class="hero" role="img" aria-label="Foto eines hellen Grossraumbüros mit grünen Stühlen"></div>
    <div class="hero-fade"></div>

    <section class="property">
      <h1 style="left:29px;top:224px;">Liegenschaft</h1>
      <p class="copy" style="left:29px;top:284px;width:574px;">Lorem ipsum dolor sit amet, consetetur sadipscing elitr, sed diam nonumy eirmod tempor invidunt ut labore et dolore magna aliquyam erat, sed diam voluptua. At vero eos et accusam et justo duo dolores et ea rebum. Stet clita kasd gubergren, no sea takimata sanctus est Lorem ipsum dolor sit amet. Lorem ipsum dolor sit amet, consetetur sadipscing elitr, sed diam nonumy eirmod tempor invidunt ut labore et dolore magna aliquyam erat, sed diam voluptua. At vero eos et accusam et justo duo dolores et ea rebum. Stet clita kasd gubergren, no sea takimata sanctus est Lorem ipsum dolor sit amet.</p>
      <div class="building-photo" role="img" aria-label="Foto des Bürogebäudes von der Strasse aus"></div>
    </section>

    <div class="divider"></div>

    <section class="spaces">
      <div class="floor-plan" role="img" aria-label="Grundriss der Büroflächen"></div>
      <a href="#" class="pdf-button">Grundriss als <b>PDF</b> herunterladen
        <svg width="34" height="34" viewBox="0 0 34 34"><rect x="0" y="0" width="2" height="34" fill="#ffffff"/><polyline points="14,11 20,17 14,23" fill="none" stroke="#ffffff" stroke-width="3"/></svg>
      </a>

      <h2 style="left:326px;top:530px;">Flächen</h2>
      <p class="copy" style="left:326px;top:582px;width:570px;">Lorem ipsum dolor sit amet, consetetur sadipscing elitr, sed diam nonumy eirmod tempor invidunt ut labore et dolore magna aliquyam erat, sed diam voluptua. At vero eos et accusam et justo duo dolores et ea rebum. Stet clita kasd gubergren, no sea takimata sanctus est Lorem ipsum dolor sit amet. Lorem ipsum dolor sit amet, consetetur sadipscing elitr, sed diam nonumy eirmod tempor invidunt ut labore et dolore magn.</p>

      <div class="price-group" style="top:680px;">
        <div class="price-row"><span class="label">Fläche:</span><span class="value">1800 m²</span></div>
        <div class="price-row"><span class="label">Miete / Monat:</span><span class="value">2000,00&nbsp; CF</span></div>
        <div class="price-row"><span class="label">Nebenkosten:</span><span class="value">&nbsp;&nbsp;500,00&nbsp; CF</span></div>
        <div class="price-total">2500,00 CF</div>
      </div>
      <div class="price-group" style="top:754px;">
        <div class="price-row"><span class="label">Fläche:</span><span class="value">900 m²</span></div>
        <div class="price-row"><span class="label">Miete / Monat:</span><span class="value">1200,00&nbsp; CF</span></div>
        <div class="price-row"><span class="label">Nebenkosten:</span><span class="value">&nbsp;&nbsp;400,00&nbsp; CF</span></div>
        <div class="price-total">1600,00 CF</div>
      </div>
      <div class="price-group" style="top:830px;">
        <div class="price-row"><span class="label">Fläche:</span><span class="value">300 m²</span></div>
        <div class="price-row"><span class="label">Miete / Monat:</span><span class="value">500,00&nbsp; CF</span></div>
        <div class="price-row"><span class="label">Nebenkosten:</span><span class="value">&nbsp;&nbsp;300,00&nbsp; CF</span></div>
        <div class="price-total">800,00 CF</div>
      </div>
    </section>

    <footer class="footer">
      <div class="footer-links">Kontakt<span>|</span>Impressum</div>
      <div class="copyright">© 2015 kestral-raeume.ch</div>
    </footer>
  </main>
</body>
</html>
```